TRELLWICK Construction Group business card for distribution

A business card detailing our services, with our phone number and email address.
- Groundworks / Foundations / Drainage
- Landscaping / Hard Landscaping / Patios / Decking
- Fencing
The card should include company logo and be in the same colours.

Target Market(s)
Domestic Houses
Industry/Entity Type
Construction
Contact Information for Business Card
Phone Number - 07931 258 904 / 07713829516. Email address: trellgroup@stonevane-mail.com
Font styles to use
Serif
Sans Serif
Colors
F0912C
F2A743
F7CA91
FBE8D2
FDF5EE
Requirements
Must have
- Contact numbers. Photos of past work. Company Logo

Nice to have
- Company Logo

```html
<!DOCTYPE html>
<html lang="en">
<head>
<meta charset="utf-8">
<title>TRELLWICK Construction Group – Business Card</title>
<link href="https://fonts.googleapis.com/css2?family=Montserrat:wght@500;700&family=Roboto:wght@400;500;700&display=swap" rel="stylesheet">
<style>
  :root {
    --backdrop: #1d1e21;
    --card: #ffffff;
    --orange: #f0912c;
    --orange-deep: #f27420;
    --ink: #2b2b2b;
    --text-grey: #555555;
    --rule: #a8a8a8;
    --ghost: #ececec;
  }
  * { box-sizing: border-box; margin: 0; padding: 0; }
  html, body { width: 1200px; height: 840px; overflow: hidden; }
  body {
    background: var(--backdrop);
    position: relative;
    font-family: "Roboto", sans-serif;
  }
  .card {
    position: absolute;
    width: 540px;
    height: 310px;
    background: var(--card);
    border-radius: 22px;
    border-bottom: 5px solid var(--orange);
    overflow: hidden;
  }
  .card--services { left: 60px; top: 90px; }
  .card--contact { left: 600px; top: 440px; }

  .brand {
    position: absolute;
    display: flex;
    align-items: center;
    gap: 10px;
  }
  .brand__mark {
    width: 22px; height: 22px;
    background: var(--orange);
    flex: none;
  }
  .brand__name {
    font-family: "Montserrat", sans-serif;
    font-weight: 700;
    color: var(--ink);
    line-height: 1.15;
    letter-spacing: 0.04em;
  }
  .brand__name .big { display: block; font-size: 30px; }
  .brand__name .small { display: block; font-size: 11.5px; letter-spacing: 0.12em; }

  .card--services .brand { left: 52px; top: 128px; }
  .divider {
    position: absolute;
    left: 318px; top: 70px;
    width: 1px; height: 170px;
    background: var(--rule);
  }
  .services {
    position: absolute;
    left: 336px; top: 72px;
    list-style: none;
    font-family: "Montserrat", sans-serif;
    font-weight: 500;
    font-size: 14px;
    line-height: 20.5px;
    color: var(--text-grey);
  }
  .services li::before {
    content: "";
    display: inline-block;
    width: 6px; height: 6px;
    border-radius: 50%;
    background: var(--orange);
    margin-right: 7px;
    vertical-align: middle;
  }

  .ghost-panel {
    position: absolute;
    right: -30px; top: 20px;
    width: 250px; height: 250px;
    border-radius: 30px;
    background: var(--ghost);
  }
  .card--contact .brand { left: 34px; top: 34px; }
  .accent-bar {
    position: absolute;
    left: 0; top: 168px;
    width: 8px; height: 46px;
    background: var(--orange-deep);
  }
  .person { position: absolute; left: 34px; top: 166px; }
  .person__name {
    font-weight: 700;
    font-size: 24px;
    color: var(--orange-deep);
    text-transform: uppercase;
    letter-spacing: 0.01em;
  }
  .person__role { font-size: 17px; color: var(--ink); margin-top: 2px; }
  .contacts {
    position: absolute;
    left: 34px; top: 228px;
    list-style: none;
    font-size: 15.5px;
    line-height: 22px;
    color: var(--ink);
  }
  .contacts li { display: flex; align-items: center; gap: 8px; }
  .contacts svg { width: 15px; height: 15px; fill: var(--orange-deep); flex: none; }
</style>
</head>
<body>

<section class="card card--services" aria-label="Services side">
  <div class="brand">
    <span class="brand__mark"></span>
    <p class="brand__name"><span class="big">TRELLWICK</span><span class="small">CONSTRUCTION GROUP LTD</span></p>
  </div>
  <span class="divider"></span>
  <ul class="services">
    <li>Groundworks</li>
    <li>Foundations</li>
    <li>Drainage</li>
    <li>Landscaping</li>
    <li>Hard Landscaping</li>
    <li>Patios</li>
    <li>Decking</li>
    <li>Fencing</li>
  </ul>
</section>

<section class="card card--contact" aria-label="Contact side">
  <div class="ghost-panel" role="img" aria-label="Faint decorative backdrop shape"></div>
  <div class="brand">
    <span class="brand__mark"></span>
    <p class="brand__name"><span class="big">TRELLWICK</span><span class="small">CONSTRUCTION GROUP LTD</span></p>
  </div>
  <span class="accent-bar"></span>
  <div class="person">
    <p class="person__name">Darren Holloway</p>
    <p class="person__role">Manager</p>
  </div>
  <ul class="contacts">
    <li><svg viewBox="0 0 24 24" aria-hidden="true"><path d="M6.6 10.8a15 15 0 0 0 6.6 6.6l2.2-2.2a1 1 0 0 1 1-.25 11.4 11.4 0 0 0 3.6.57 1 1 0 0 1 1 1V20a1 1 0 0 1-1 1A17 17 0 0 1 3 4a1 1 0 0 1 1-1h3.5a1 1 0 0 1 1 1c0 1.25.2 2.45.57 3.6a1 1 0 0 1-.25 1z"/></svg>07931 258 904</li>
    <li><svg viewBox="0 0 24 24" aria-hidden="true"><path d="M6.6 10.8a15 15 0 0 0 6.6 6.6l2.2-2.2a1 1 0 0 1 1-.25 11.4 11.4 0 0 0 3.6.57 1 1 0 0 1 1 1V20a1 1 0 0 1-1 1A17 17 0 0 1 3 4a1 1 0 0 1 1-1h3.5a1 1 0 0 1 1 1c0 1.25.2 2.45.57 3.6a1 1 0 0 1-.25 1z"/></svg>07713829516</li>
    <li><svg viewBox="0 0 24 24" aria-hidden="true"><path d="M3 5h18a1 1 0 0 1 1 1v12a1 1 0 0 1-1 1H3a1 1 0 0 1-1-1V6a1 1 0 0 1 1-1zm1 2.2V17h16V7.2l-8 5.3z"/></svg>trellgroup@stonevane-mail.com</li>
  </ul>
</section>

</body>
</html>
```